Sports medicine multidisciplinary brochures

Multi-disciplinary sports medicine clinic. Need a range of pamphlet / foldable brochures to advertise our various services. Looking at keeping a similar 'look' between the various brochures to still ID as being part of the group, but perhaps slight colour variation / different front pic to distinguish them. Looking at a pamphlet for: 1) General clinic (about us) info 2) Concussion info 3) Podiatry 4) Sports Physicians 5) Exercise Physiology 6) Osteoarthritis 7) Physiotherapy. Modern feel, but still warm / inviting. See attached logo / cards / etc. Thank you!

Target Market(s)

Athletes, sports injuries + general health / medical

Industry/Entity Type

Clinic

Requirements
Nice to have
• Simple, warm design. Activity / health / lifestyle related feel.
• Design to allow easy adaptation of wording / content.

```html
<!DOCTYPE html>
<html lang="en">
<head>
<meta charset="utf-8">
<title>Kineta Sports &amp; Joint Clinic – Trifold Brochure</title>
<link href="https://fonts.googleapis.com/css2?family=Lato:wght@400;700&family=Open+Sans:wght@400;600&family=Roboto+Slab:wght@700&family=Varela+Round&display=swap" rel="stylesheet">
<style>
  :root {
    --yellow: #f7c51c;
    --orange: #f39a1e;
    --orange-deep: #ee8a14;
    --green: #1f9d5b;
    --green-light: #3bb54a;
    --grey-dark: #3a3a3a;
    --grey-mid: #6a6a6a;
    --white: #ffffff;
    --ink: #1d1d1d;
    --text-grey: #4a4a4a;
  }
  * { margin: 0; padding: 0; box-sizing: border-box; }
  html, body { width: 1200px; height: 848px; overflow: hidden; background: #ffffff; }
  .brochure { position: relative; width: 1200px; height: 848px; overflow: hidden; }
  .brochure-shapes { position: absolute; inset: 0; }

  .section-tab {
    position: absolute; left: 0; height: 36px; padding: 0 30px 0 26px;
    background: var(--green); color: var(--white);
    font: 700 21px/36px "Roboto Slab", serif;
    border-radius: 0 18px 18px 0;
    box-shadow: 3px 0 0 var(--white);
  }
  .about-tab { top: 44px; }
  .hours-tab { top: 278px; }

  .about-text {
    position: absolute; left: 24px; top: 94px; width: 344px;
    font: 700 12.4px/15.8px "Lato", sans-serif; color: var(--ink);
    text-align: justify;
  }

  .hours-table {
    position: absolute; left: 28px; top: 338px; width: 338px;
    border: 1.5px solid #5a4a1a; border-radius: 10px; border-collapse: separate;
    border-spacing: 0; overflow: hidden;
    font: 400 13.5px "Lato", sans-serif; color: var(--ink);
  }
  .hours-table td { height: 34px; text-align: center; border-bottom: 1.5px solid #5a4a1a; }
  .hours-table tr:last-child td { border-bottom: none; }
  .hours-table td:first-child { width: 170px; border-right: 1.5px solid #5a4a1a; }
  .time-pill {
    display: inline-block; padding: 2px 8px; background: var(--green);
    color: var(--white); font-weight: 700; font-size: 13px; border: 1px solid #e8f5ea;
  }

  .hours-note {
    position: absolute; left: 36px; top: 494px; width: 320px; text-align: center;
    font: 700 12.5px/15.5px "Lato", sans-serif; color: #3a2a08;
  }

  .contact-box {
    position: absolute; left: 442px; top: 427px; width: 304px; height: 136px;
    border: 2px solid var(--yellow); border-radius: 10px;
    font-family: "Open Sans", sans-serif; color: var(--white); text-align: center;
    padding-top: 14px;
  }
  .contact-email { font-size: 15px; }
  .contact-phone { font-size: 21px; margin: 4px 0 8px; letter-spacing: 0.5px; }
  .contact-address { font-size: 14.5px; line-height: 18px; }

  .brand-name {
    position: absolute; font: 400 26px "Varela Round", sans-serif;
    color: var(--green); letter-spacing: 2px; text-align: center;
  }
  .brand-back { left: 480px; top: 690px; width: 160px; font-size: 23px; }
  .brand-front { left: 1010px; top: 160px; width: 180px; font-size: 34px; }

  .web-address {
    position: absolute; font: 600 13px "Open Sans", sans-serif; letter-spacing: 1px;
  }
  .web-back { left: 400px; width: 390px; top: 793px; text-align: center; color: var(--white); }
  .web-front { left: 800px; width: 400px; top: 800px; text-align: center; color: #222; }

  .cover-title {
    position: absolute; left: 800px; width: 400px; top: 555px; text-align: center;
    font: 400 44px "Varela Round", sans-serif; color: var(--orange); font-weight: 700;
  }
  .cover-subtitle {
    position: absolute; left: 800px; width: 400px; top: 612px; text-align: center;
    font: 400 29px "Varela Round", sans-serif; color: var(--text-grey);
  }
  .cover-text {
    position: absolute; left: 840px; width: 320px; top: 660px; text-align: center;
    font: 600 16px/20px "Open Sans", sans-serif; color: var(--green);
  }
</style>
</head>
<body>
<main class="brochure">
  <svg class="brochure-shapes" width="1200" height="848" viewBox="0 0 1200 848" xmlns="http://www.w3.org/2000/svg">
    <defs>
      <linearGradient id="panelYellow" x1="0" y1="0" x2="1" y2="1">
        <stop offset="0" stop-color="#f9d423"/>
        <stop offset="1" stop-color="#f6a21c"/>
      </linearGradient>
      <linearGradient id="panelGrey" x1="0" y1="0" x2="1" y2="0">
        <stop offset="0" stop-color="#2e2e2e"/>
        <stop offset="0.6" stop-color="#6e6e6e"/>
        <stop offset="1" stop-color="#4a4a4a"/>
      </linearGradient>
      <linearGradient id="parkPhoto" x1="0" y1="0" x2="0" y2="1">
        <stop offset="0" stop-color="#7a9a3a"/>
        <stop offset="0.45" stop-color="#4f7d2a"/>
        <stop offset="1" stop-color="#6fae3a"/>
      </linearGradient>
      <linearGradient id="familyPhoto" x1="0" y1="0" x2="1" y2="1">
        <stop offset="0" stop-color="#d8cfc6"/>
        <stop offset="0.5" stop-color="#a9b3c2"/>
        <stop offset="1" stop-color="#5d7392"/>
      </linearGradient>
      <linearGradient id="bandOrange" x1="0" y1="0" x2="1" y2="0">
        <stop offset="0" stop-color="#f7b21e"/>
        <stop offset="1" stop-color="#ef8914"/>
      </linearGradient>
    </defs>

    <!-- left panel -->
    <rect class="panel-inside-left" x="0" y="0" width="392" height="848" fill="url(#panelYellow)"/>
    <path d="M0 848 L0 660 C60 600 200 570 350 560 C380 620 395 720 392 848 Z" fill="var(--green)"/>
    <path d="M0 848 L0 676 C60 616 200 586 346 578 C372 636 384 730 380 848 Z" fill="var(--white)"/>
    <g role="img" aria-label="Photo of a smiling family with a baby sitting together at home">
      <path d="M14 848 L14 690 C70 632 200 600 336 594 C360 650 370 740 366 848 Z" fill="url(#familyPhoto)"/>
    </g>

    <!-- middle and right panels -->
    <rect x="392" y="0" width="808" height="848" fill="var(--white)"/>
    <rect class="panel-back" x="392" y="0" width="398" height="848" fill="url(#panelGrey)"/>

    <!-- photo swoosh -->
    <path d="M470 0 C440 160 600 380 790 470 C900 520 1020 520 1200 440 L1200 0 Z" fill="var(--white)"/>
    <path d="M500 0 C470 160 620 380 800 460 C900 505 1010 505 1200 425 L1200 0 Z" fill="var(--green)"/>
    <path d="M520 0 C496 150 640 360 810 440 C905 485 1010 485 1200 410 L1200 0 Z" fill="var(--orange)"/>
    <g role="img" aria-label="Photo of a woman meditating cross-legged on a yoga mat in a sunny park">
      <path d="M540 0 C520 140 660 345 820 420 C910 462 1010 462 1200 392 L1200 0 Z" fill="url(#parkPhoto)"/>
    </g>

    <!-- front logo circle -->
    <circle cx="1100" cy="150" r="112" fill="var(--white)"/>
    <circle cx="1100" cy="110" r="14" fill="var(--orange)"/>

    <!-- back logo circle -->
    <path d="M400 790 C520 740 680 745 790 770 L790 848 L400 848 Z" fill="var(--green)"/>
    <path d="M400 770 C520 730 660 730 790 756 L790 770 C680 745 520 742 400 784 Z" fill="var(--green-light)"/>
    <circle cx="560" cy="690" r="78" fill="var(--orange)"/>
    <circle cx="560" cy="690" r="70" fill="var(--white)"/>
    <circle cx="560" cy="660" r="12" fill="var(--orange)"/>

    <!-- front bottom band -->
    <path d="M790 790 C900 740 1060 730 1200 760 L1200 848 L790 848 Z" fill="var(--green)"/>
    <path d="M790 800 C900 756 1060 748 1200 776 L1200 848 L790 848 Z" fill="url(#bandOrange)"/>
  </svg>

  <!-- inside left panel -->
  <h2 class="section-tab about-tab">ABOUT US:</h2>
  <p class="about-text">kineta sports &amp; joint clinic (kineta) is a new multidisciplinary clinic with specialist sports and exercise physicians as the leads. this is unique in adelaide, aiming to provide affordable, evidence based, non-surgical treatment for sport and musculoskeletal injuries, as well as osteoarthritis. combining specialist physician overview with select physiotherapists, podiatry, and other allied health integrated with use of our new fully equipped gym and modern software, kineta is uniquely positioned to work with you.</p>

  <h2 class="section-tab hours-tab">OPENING HOURS</h2>
  <table class="hours-table">
    <tr><td>Monday - Wednesday</td><td><span class="time-pill">8:30 - 6</span></td></tr>
    <tr><td>Thursday</td><td><span class="time-pill">8:30 - 8</span></td></tr>
    <tr><td>Friday</td><td><span class="time-pill">8:30 - 3</span></td></tr>
    <tr><td>Saturday</td><td><span class="time-pill">9 - 12:30</span></td></tr>
  </table>
  <p class="hours-note">Contrary to popular belief, Lorem Ipsum is not simply random text. It has roots in a piece of classical Latin litarature.</p>

  <!-- back panel -->
  <address class="contact-box">
    <div class="contact-email">EMAIL: hello@kinetaclinic.com.au</div>
    <div class="contact-phone">CALL US: 08 5550 1234</div>
    <div class="contact-address">Kineta Sports &amp; Joint Clinic<br>12 Harbour View Rd, Westfield 5099</div>
  </address>
  <div class="brand-name brand-back">KINETA</div>
  <div class="web-address web-back">www.kinetaclinic.com</div>

  <!-- front cover -->
  <div class="brand-name brand-front">KINETA</div>
  <h1 class="cover-title">Lorem Ipsum</h1>
  <p class="cover-subtitle">is simply dummy text</p>
  <p class="cover-text">Contrary to popular belief, Lorem Ipsum is not simply random text. It has roots in a piece of classical Latin litarature.</p>
  <div class="web-address web-front">www.kinetaclinic.com</div>
</main>
</body>
</html>
```